Veltrix88 Web Site

We need a new web site for a new company, Veltrix88 Pty Ltd.
The company will provide services around the Orvane Sky and Plinth 540 products.
The company theme is "Work is what you do, not where you go." We aim to separate the concepts of data and place. Our clients can access their data anywhere, any time.
The design should look modern, international and should include the Orvane Associate logo.
Updates
My existing web site is visible at http://kelvaro.net.au. I am hoping that a good designer can provide a fresh look for the business.
Three images for "Cloud" uploaded today.
Target Market(s)
Business of all kinds
Industry/Entity Type
It Company
Requirements
Nice to have
- Colors and themes might reflect Orvane look and style.

```html
<!DOCTYPE html>
<html lang="en">
<head>
<meta charset="utf-8">
<title>Veltrix88 — Cloud Data Anywhere</title>
<link rel="stylesheet" href="https://fonts.googleapis.com/css2?family=Open+Sans:wdth,wght@75..100,300..800&display=swap">
<style>
  :root {
    --navy: #1b2b4b;
    --brand-blue: #1f4e79;
    --accent-blue: #1a7fc8;
    --link-blue: #1a8ad4;
    --ink: #444444;
    --muted: #666666;
    --nav-grey: #8a8a8a;
    --band-grey: #d6d6d6;
    --frame: #c9d3dc;
  }
  * { box-sizing: border-box; margin: 0; padding: 0; }
  html, body { width: 1200px; height: 1000px; overflow: hidden; background: #ffffff; }
  body { position: relative; font-family: "Open Sans", Arial, sans-serif; color: var(--ink); }

  .top-rule { position: absolute; left: 0; top: 0; width: 1200px; height: 6px; background: var(--navy); }

  .contact-tab { position: absolute; left: 680px; top: 6px; width: 408px; height: 34px; }
  .contact-tab svg.tab-shape { position: absolute; inset: 0; }
  .contact-line { position: absolute; left: 32px; top: 0; height: 34px; display: flex; align-items: center; gap: 24px; color: #ffffff; font-weight: 600; font-size: 15px; }
  .contact-line .phone { display: flex; align-items: center; gap: 12px; }

  .brand { position: absolute; left: 130px; top: 30px; display: flex; align-items: center; gap: 16px; }
  .brand-mark { width: 52px; height: 52px; background: var(--brand-blue); }
  .brand-name { font-size: 32px; font-weight: 700; color: var(--brand-blue); letter-spacing: 0.5px; }

  .main-nav { position: absolute; top: 56px; right: 123px; display: flex; gap: 0; }
  .main-nav a { font-size: 14px; font-weight: 600; color: var(--nav-grey); text-decoration: none; margin-left: 24px; }
  .main-nav a.current { color: var(--ink); font-weight: 700; margin-right: 8px; }

  .hero { position: absolute; left: 130px; top: 106px; width: 940px; height: 410px; border: 1px solid var(--frame);
    background: linear-gradient(90deg, #2d4f86 0%, #4c74ad 30%, #8fb3dc 55%, #cfe2f5 75%, #e6f0fa 100%); overflow: hidden; }
  .hero-photo { position: absolute; left: 0; top: 0; width: 560px; height: 410px; }
  .hero-copy { position: absolute; left: 558px; top: 116px; }
  .hero-title { font-stretch: 75%; font-weight: 700; font-size: 42px; color: #3d3d3d; line-height: 1; letter-spacing: -0.5px; }
  .hero-title span { color: var(--accent-blue); }
  .hero-lead { margin: 14px 0 0 2px; font-size: 19px; line-height: 25px; color: #333; font-weight: 400; }
  .hero-lead strong { font-weight: 700; }
  .hero-button { position: absolute; left: 2px; top: 136px; width: 140px; height: 46px; border: 1px solid #2a7fc0;
    background: linear-gradient(#5bb6ee, #2b8ed6); color: #fff; font-weight: 700; font-size: 16px; display: flex; align-items: center; justify-content: center; }
  .slide-dots { position: absolute; left: 434px; top: 376px; display: flex; gap: 10px; }
  .slide-dots i { width: 10px; height: 10px; border-radius: 50%; background: rgba(255,255,255,0.55); }
  .slide-dots i.active { background: #ffffff; }

  .services { position: absolute; left: 130px; top: 536px; display: flex; gap: 20px; }
  .service { width: 220px; position: relative; height: 330px; }
  .service h2 { font-stretch: 75%; font-weight: 700; font-size: 22px; color: #3d3d3d; line-height: 28px; }
  .service .thumb { margin-top: 6px; width: 220px; height: 143px; }
  .service h3 { margin-top: 14px; font-size: 12px; font-weight: 700; color: #5a5a5a; white-space: nowrap; }
  .service p { margin-top: 18px; font-size: 12.5px; line-height: 18px; color: var(--muted); }
  .service .more { position: absolute; left: 2px; top: 312px; font-size: 13px; color: var(--link-blue); text-decoration: none; font-weight: 500; }

  .thumb-datacentre { background: linear-gradient(90deg, #e9ecef, #9aa2ab 20%, #f2f4f6 40%, #b8bec5 60%, #f5f6f8 85%, #ffffff); }
  .thumb-technician { background: linear-gradient(90deg, #cfd2d6 0%, #3a3a3e 35%, #2a2a2e 60%, #6b5e63 85%, #4a4048); }
  .thumb-cloud { background: radial-gradient(ellipse at 60% 40%, #bfe6fa 0%, #4fb6ea 45%, #2b8fd2 75%, #ffffff 100%); }
  .thumb-suite { background: linear-gradient(180deg, #ffffff 0%, #ffffff 55%, #fde0b0 75%, #f39a2a 100%); }

  .testimonials { position: absolute; left: 27px; top: 910px; width: 1150px; height: 200px; background: var(--band-grey); }
  .testimonials h2 { position: absolute; left: 0; top: 28px; width: 100%; text-align: center; font-stretch: 75%; font-weight: 700; font-size: 24px; color: #444; }
  .quote { position: absolute; top: 76px; width: 300px; font-size: 15px; color: #555; line-height: 22px; white-space: nowrap; }
</style>
</head>
<body>
  <div class="top-rule"></div>

  <div class="contact-tab">
    <svg class="tab-shape" width="408" height="34" viewBox="0 0 408 34"><polygon points="0,0 408,0 398,34 10,34" fill="#1b2b4b"/></svg>
    <div class="contact-line">
      <span class="phone">
        <svg width="24" height="24" viewBox="0 0 24 24"><circle cx="12" cy="12" r="10.5" fill="none" stroke="#7f94b5" stroke-width="1.5"/><path d="M8.5 6.5 l2 2.5 -1.2 1.4 c0.7 1.6 1.8 2.8 3.3 3.6 l1.4 -1.2 2.5 2 -1.3 2 c-4 -0.5 -7.5 -4 -8.2 -8.2z" fill="#7f94b5"/></svg>
        08 9417 2250
      </span>
      <span>service@veltrix88.com.au</span>
    </div>
  </div>

  <div class="brand">
    <div class="brand-mark"></div>
    <div class="brand-name">VELTRIX88</div>
  </div>

  <nav class="main-nav">
    <a class="current" href="#">Home</a>
    <a href="#">Cloud Service</a>
    <a href="#">Emergency Services</a>
    <a href="#">About</a>
    <a href="#">Contact</a>
  </nav>

  <section class="hero">
    <div class="hero-photo" role="img" aria-label="Businessman in a suit using a tablet, blue-toned photograph"></div>
    <div class="hero-copy">
      <h1 class="hero-title">Cloud Data <span>Anywhere.</span></h1>
      <p class="hero-lead">We help your business and your<br>people work <strong>anywhere, anytime.</strong></p>
      <a class="hero-button">Read More</a>
    </div>
    <div class="slide-dots"><i class="active"></i><i></i><i></i><i></i></div>
  </section>

  <section class="services">
    <article class="service">
      <h2>Cloud Services</h2>
      <div class="thumb thumb-datacentre" role="img" aria-label="Rows of server racks in a bright data centre"></div>
      <h3>Safe and Secure</h3>
      <p>Work is what you do, not where you do it. Access your files, anywhere, anytime.</p>
      <a class="more" href="#">Find out more...</a>
    </article>
    <article class="service">
      <h2>Emergency Services</h2>
      <div class="thumb thumb-technician" role="img" aria-label="Technician working on network cabling in a server rack"></div>
      <h3>Emergency Disk Recovery</h3>
      <p>Some information is like gold to your business. We can recover data from corrupted disks.</p>
      <a class="more" href="#">Find out more...</a>
    </article>
    <article class="service">
      <h2>Orvane Sky</h2>
      <div class="thumb thumb-cloud" role="img" aria-label="Blue cloud illustration with a golden swoosh"></div>
      <h3>Worldwide data at your fingertips</h3>
      <p>Activate Orvane's Cloud services. Available around the clock.</p>
      <a class="more" href="#">Find out more...</a>
    </article>
    <article class="service">
      <h2>Plinth 540</h2>
      <div class="thumb thumb-suite" role="img" aria-label="Plinth 540 product banner with orange waves"></div>
      <h3>Plinth540 is anywhere you want it to be</h3>
      <p>Get virtually anywhere access to the Orvane Office tools you know and rely on, plus easy to administer business-class IT services.</p>
      <a class="more" href="#">Find out more...</a>
    </article>
  </section>

  <section class="testimonials">
    <h2>What Our Clients Say</h2>
    <p class="quote" style="left:103px">“It's a pleasure dealing with such</p>
    <p class="quote" style="left:423px">“I like your creed, service is so important. As</p>
    <p class="quote" style="left:743px">Thank you for all your wonderful support -</p>
  </section>
</body>
</html>
```